Construction Company Business Card

Business Card Design using new Logo

Contact Information for Business Card

include all company info and website

Requirements
Must have
• Wesley Corman - President
ph. 254-617-0382
Cedar Knoll, TX
wesley@ironmarkframing.com
www.ironmarkframing.com

```html
<!DOCTYPE html>
<html lang="en">
<head>
<meta charset="utf-8">
<title>Ironmark Framing — Business Card</title>
<link rel="stylesheet" href="https://fonts.googleapis.com/css2?family=Poppins:wght@400;500;600;700&display=swap">
<style>
  :root {
    --stage: #ebebeb;
    --paper: #ffffff;
    --card: #2c2c2e;
    --peach: #f0bfa3;
    --peach-deep: #e39f7e;
    --chalk: #f2f2f0;
    --navy: #1d2b33;
  }
  * { box-sizing: border-box; margin: 0; padding: 0; }
  html, body { width: 1200px; height: 1200px; overflow: hidden; }
  body {
    font-family: "Poppins", sans-serif;
    background: var(--stage);
    position: relative;
  }
  .card {
    position: absolute;
    left: 250px;
    width: 700px;
    height: 400px;
    background: var(--card);
    overflow: hidden;
    box-shadow: 0 10px 28px rgba(0,0,0,.18);
  }
  .card--back { top: 70px; }
  .card--front { top: 500px; }

  .accent-panel {
    position: absolute;
    top: 0;
    height: 400px;
    background: linear-gradient(160deg, var(--peach) 0%, #e8cdbd 55%, var(--chalk) 100%);
  }
  .card--back .accent-panel { right: 0; width: 200px; }
  .card--front .accent-panel { left: 0; width: 180px; }

  /* back */
  .back-brand {
    position: absolute; left: 40px; top: 36px;
    color: var(--peach); font-weight: 600; font-size: 18px;
  }
  .person { position: absolute; left: 40px; top: 230px; }
  .person__name { color: var(--chalk); font-weight: 600; font-size: 20px; }
  .person__role { color: var(--peach); font-weight: 500; font-size: 15px; margin-top: 2px; }
  .contacts {
    position: absolute; left: 250px; top: 200px; list-style: none;
    color: var(--chalk); font-size: 13px; line-height: 25px;
  }
  .contacts li { display: flex; align-items: center; gap: 10px; }
  .contacts svg { width: 12px; height: 12px; fill: var(--peach); flex: none; }

  /* front */
  .front-brand {
    position: absolute; left: 290px; top: 0; height: 400px; right: 40px;
    display: flex; align-items: center; justify-content: flex-end; gap: 12px;
    color: var(--peach); font-weight: 600; font-size: 34px;
  }
  .front-brand__mark { width: 22px; height: 22px; background: var(--peach); flex: none; }

  /* wordmark showcase */
  .showcase {
    position: absolute; left: 0; top: 960px; width: 1200px; height: 240px;
    background: var(--paper);
    display: flex; align-items: center; justify-content: center; gap: 14px;
  }
  .showcase__mark { width: 30px; height: 30px; background: var(--peach-deep); }
  .showcase__name { color: var(--peach-deep); font-weight: 600; font-size: 46px; }
</style>
</head>
<body>

  <section class="card card--back" aria-label="Business card, back">
    <div class="back-brand">ironmarkframing</div>
    <div class="person">
      <p class="person__name">Wesley Corman</p>
      <p class="person__role">President</p>
    </div>
    <ul class="contacts">
      <li><svg viewBox="0 0 12 12" aria-hidden="true"><path d="M6 0a4 4 0 0 0-4 4c0 3 4 8 4 8s4-5 4-8a4 4 0 0 0-4-4zm0 5.5A1.5 1.5 0 1 1 6 2.5a1.5 1.5 0 0 1 0 3z"/></svg>Cedar Knoll, TX</li>
      <li><svg viewBox="0 0 12 12" aria-hidden="true"><path d="M2.5 0l2 3-1.2 1.3a7 7 0 0 0 4.4 4.4L9 7.5l3 2-1.5 2.5C5 12 0 7 0 1.5z"/></svg>254-617-0382</li>
      <li><svg viewBox="0 0 12 12" aria-hidden="true"><path d="M0 2h12v8H0zm1 1v.3l5 3.2 5-3.2V3z"/></svg>wesley@ironmarkframing.com</li>
      <li><svg viewBox="0 0 12 12" aria-hidden="true"><circle cx="6" cy="6" r="5.5"/></svg>www.ironmarkframing.com</li>
    </ul>
    <div class="accent-panel" role="img" aria-label="Decorative geometric pattern in peach, white and navy"></div>
  </section>

  <section class="card card--front" aria-label="Business card, front">
    <div class="accent-panel" role="img" aria-label="Decorative geometric pattern in peach, white and navy"></div>
    <div class="front-brand">
      <span class="front-brand__mark"></span>
      <span class="front-brand__name">ironmarkframing</span>
    </div>
  </section>

  <section class="showcase" aria-label="Company name">
    <span class="showcase__mark"></span>
    <span class="showcase__name">ironmarkframing</span>
  </section>

</body>
</html>
```